Brightfold Partners Website

Brightfold Partners Advisory Services is a company which provides specialised advise in carbon markets, climate policy, landscapes, resilience and change. We are based in Australia but the majority of our business is global. Our clients range from governments to large corporates and not for profit organisations.
Our focus is on developing the capabilities of government officials, business decision makers and land managers so they can better navigate the complexity of climate change and sustainability.
We are looking for a website that is consistent with the high end professional services which we provide to serious players.
I have attached two versions of our logo. I have also attached the back of our business card so you can get a sense of what we hand to potential clients.

Target Market(s)

Professional individuals, decision makers, board members etc, government officials.

Industry/Entity Type

Government

Number of Pages Required

4 page

Font styles to use
Serif
Sans Serif

Requirements
Must have
• Please provide
• 1. Home page
• 2. Service page template
• 3. Contact page
• 4. Lead expert profile page

```html
<!DOCTYPE html>
<html lang="en">
<head>
<meta charset="utf-8">
<title>Brightfold Partners</title>
<link href="https://fonts.googleapis.com/css2?family=Mulish:wght@300;400;600&family=Open+Sans:wght@400;600&display=swap" rel="stylesheet">
<style>
:root{
  --ink:#2d3033;
  --muted:#6b6f73;
  --band:#f4f4f4;
  --steel:#4f7596;
  --steel-dark:#3a5a76;
  --gold:#e3ac3a;
  --gold-ink:#3a2a0c;
  --orange:#f79a12;
  --footer:#22282b;
  --footer-base:#2a3033;
  --white:#ffffff;
}
*{margin:0;padding:0;box-sizing:border-box}
html,body{width:809px;height:1200px;overflow:hidden;background:var(--white)}
body{position:relative;font-family:"Open Sans",sans-serif;color:var(--ink)}

.site-header{position:absolute;left:0;top:0;width:809px;height:75px;background:var(--white)}
.brand{position:absolute;left:120px;top:19px;display:flex;align-items:center;gap:9px}
.brand-dot{width:32px;height:32px;border-radius:50%;background:#8a8d90}
.brand-name{font-family:"Mulish",sans-serif;font-weight:600;font-size:17px;line-height:19px;letter-spacing:2.6px;color:#3a3c3e;text-transform:uppercase}
.main-nav{position:absolute;top:35px;left:332px;display:flex;gap:19px;font-family:"Mulish",sans-serif;font-size:10px;font-weight:600;color:#2b2d2f;letter-spacing:.2px}

.hero{position:absolute;left:0;top:75px;width:809px;height:340px;background:linear-gradient(180deg,#74aede 0%,#a9cbe6 35%,#c7d2da 62%,#8b7f6c 82%,#6f5a40 100%)}
.hero-callout{position:absolute;left:118px;top:103px;width:237px;height:106px;background:var(--gold);padding:22px 22px 0 23px;color:var(--white);overflow:hidden}
.hero-callout .kicker{font-family:"Mulish",sans-serif;font-size:14.5px;font-weight:400;line-height:17px;color:var(--gold-ink);white-space:nowrap}
.hero-callout h1{font-family:"Mulish",sans-serif;font-size:20px;font-weight:400;line-height:24px;white-space:nowrap}
.hero-callout p{font-size:7px;line-height:11px;margin-top:4px;padding-left:2px}
.slider-dots{position:absolute;left:379px;top:322px;display:flex;gap:3px}
.slider-dots span{width:7px;height:7px;border-radius:50%;background:var(--white)}

.features{position:absolute;left:0;top:415px;width:809px;height:187px;background:var(--band)}
.feature{position:absolute;top:25px;width:170px;text-align:center}
.feature svg{display:block;margin:0 auto;height:54px}
.feature h3{font-family:"Mulish",sans-serif;font-weight:400;font-size:13px;margin-top:9px;color:#2d3033}
.feature p{font-size:6.6px;line-height:11px;color:var(--muted);margin-top:3px}
.btn-steel{display:inline-block;margin-top:8px;width:66px;height:19px;line-height:19px;border-radius:2px;background:linear-gradient(#5e86a8,var(--steel-dark));color:var(--white);font-size:6.6px;font-weight:600}

.about{position:absolute;left:130px;top:632px;width:549px;text-align:center}
.about h2{font-family:"Mulish",sans-serif;font-weight:300;font-size:24px;color:#2b2d2f}
.about p{font-size:7px;line-height:13px;color:#4a4d50;margin-top:7px}
.about p+p{margin-top:5px}

.card{position:absolute;top:784px;width:182px}
.card-img{width:182px;height:77px}
.card h3{font-family:"Mulish",sans-serif;font-weight:600;font-size:11.5px;margin-top:10px;color:#34373a}
.card p{font-size:6.6px;line-height:12px;color:var(--muted);margin-top:4px}
.btn-orange{display:inline-block;margin-top:5px;width:63px;height:19px;line-height:19px;text-align:center;background:linear-gradient(#fbb034,var(--orange));color:var(--white);font-size:6.6px;border-radius:2px}

.site-footer{position:absolute;left:0;top:1000px;width:809px;height:160px;background:var(--footer);color:#e9eaeb}
.footer-col{position:absolute;top:27px}
.footer-col h4{font-family:"Mulish",sans-serif;font-weight:400;font-size:12px;margin-bottom:6px}
.footer-col li{list-style:none;font-size:7px;line-height:16.5px}
.social{display:flex;gap:3px;margin-top:3px}
.social span{width:15px;height:15px;border-radius:50%;background:var(--white)}
.footer-base{position:absolute;left:0;top:1160px;width:809px;height:40px;background:var(--footer-base);border-top:1px solid #3a4044}
.footer-base p{position:absolute;left:118px;top:17px;font-size:6.6px;color:#c9cbcd}
</style>
</head>
<body>

<header class="site-header">
  <div class="brand">
    <span class="brand-dot"></span>
    <span class="brand-name">Brightfold<br>Partners</span>
  </div>
  <nav class="main-nav">
    <span>ABOUT</span><span>SERVICES</span><span>PROJECTS</span><span>TESTIMONIAL</span><span>CLIENT</span><span>CONTACT</span>
  </nav>
</header>

<section class="hero" role="img" aria-label="Power station chimneys releasing smoke under a blue cloudy sky">
  <div class="hero-callout">
    <div class="kicker">ADVISORY SERVICES IN</div>
    <h1>CARBON MARKETS</h1>
    <p>Dis parturient montes nascetur ridiculus mus In iac ulis facilisis massa Etiam eu urna Sed</p>
  </div>
  <div class="slider-dots"><span></span><span></span><span></span><span></span></div>
</section>

<section class="features">
  <div class="feature" style="left:129px">
    <svg viewBox="0 0 60 54" fill="none" stroke="#4f7596" stroke-width="2.5">
      <path d="M14 38a10 10 0 0 1 1-20 14 14 0 0 1 27-3 10 10 0 0 1 6 19"/>
      <path d="M30 18v24M20 30h20M23 23l14 14M37 23L23 37"/>
      <circle cx="50" cy="42" r="2.5" fill="#4f7596"/><circle cx="45" cy="49" r="2.5" fill="#4f7596"/>
    </svg>
    <h3>Featured Service</h3>
    <p>dis parturient montes nascetur ridiculus mus In iaculis facilisis massa Etiam eu urna Sed</p>
    <span class="btn-steel">READ MORE</span>
  </div>
  <div class="feature" style="left:313px">
    <svg viewBox="0 0 60 54" fill="none" stroke="#4f7596" stroke-width="3">
      <circle cx="30" cy="17" r="10"/><circle cx="19" cy="35" r="10"/><circle cx="41" cy="35" r="10"/>
      <circle cx="30" cy="29" r="4" fill="#4f7596"/>
    </svg>
    <h3>Featured Service</h3>
    <p>dis parturient montes nascetur ridiculus mus In iaculis facilisis massa Etiam eu urna</p>
    <span class="btn-steel">READ MORE</span>
  </div>
  <div class="feature" style="left:499px">
    <svg viewBox="0 0 60 54">
      <path d="M14 52V42c-6-4-8-10-6-18 3-10 14-14 22-10 6 3 9 9 8 16l4 7h-5v6h-9v9z" fill="#4f7596"/>
      <circle cx="30" cy="23" r="6" fill="none" stroke="#fff" stroke-width="2"/>
      <circle cx="45" cy="12" r="6" fill="none" stroke="#4f7596" stroke-width="3"/>
    </svg>
    <h3>Featured Service</h3>
    <p>dis parturient montes nascetur ridiculus mus In iaculis facilisis massa Etiam eu urna Sed</p>
    <span class="btn-steel">READ MORE</span>
  </div>
</section>

<section class="about">
  <h2>About Our Company</h2>
  <p>Mauris vel lacus vitae felis vestibulum volutpat Etiam est nunc venenatis in tristique eu imperdiet ac nisl Cum sociis natoque penatibus et magnis dis parturient montes nascetur ridiculus mus In iaculis facilisis massa Etiam eu urna Sed porta Suspendisse quam leo molestie</p>
  <p>Suspendisse vulputate aliquam dui Nulla elementum dui ut augue Aliquam vehicula mi at mauris Maecenas placerat nisl at consequat rhoncus sem nunc gravida justo quis eleifend arcu velit quis lacus Morbi magna magna Fusce id felis Vivamus sollicitudin Lorem ipsum dolor sit amet consectetuer adipiscing elit Nam cursus Morbi ut mi Nullam enim leo egestas id condimentum at laoreet mattis massa</p>
</section>

<article class="card" style="left:118px">
  <div class="card-img" role="img" aria-label="Coastal cliffs with a lighthouse" style="background:linear-gradient(180deg,#8fb0cc 0%,#b9c9d3 40%,#6f8a4a 65%,#5c4a32 100%)"></div>
  <h3>WHAT WE DO</h3>
  <p>Suspendisse vulputate aliquam dui Nulla elementum dui ut augue Aliquam vehicula mi at mauris Fusce ultricies orci ac feugiat suscipit leo massa sodal</p>
  <span class="btn-orange">READ MORE</span>
</article>
<article class="card" style="left:313px">
  <div class="card-img" role="img" aria-label="Business people in a meeting" style="background:linear-gradient(90deg,#1f2b3a 0%,#c9d6e2 45%,#e8eef3 70%,#8d97a3 100%)"></div>
  <h3>CORPORATE ADVISORY</h3>
  <p>Suspendisse vulputate aliquam dui Nulla elementum dui ut augue Aliquam vehicula mi at mauris Fusce ultricies orci ac feugiat suscipit leo</p>
  <span class="btn-orange">READ MORE</span>
</article>
<article class="card" style="left:508px">
  <div class="card-img" role="img" aria-label="Training session with a worker in a hard hat" style="background:linear-gradient(90deg,#c9a66a 0%,#d9c49a 45%,#e08a3a 75%,#7c6a4e 100%)"></div>
  <h3>TRAINING &amp; COACHING</h3>
  <p>Suspendisse vulputate aliquam dui Nulla elementum dui ut augue Aliquam vehicula mi at mauris Fusce ultricies orci ac feugiat suscipit leo</p>
  <span class="btn-orange">READ MORE</span>
</article>

<footer class="site-footer">
  <div class="footer-col" style="left:123px"><h4>Who we are</h4><ul><li>About Us</li><li>How it Works</li><li>Blog</li></ul></div>
  <div class="footer-col" style="left:224px"><h4>Services</h4><ul><li>Suspendisse vulputate</li><li>Aliquam dui</li><li>Nulla elementum</li><li>Dui ut augue</li></ul></div>
  <div class="footer-col" style="left:333px"><h4>Support</h4><ul><li>Aliquam vehicula</li><li>Maecenas</li><li>Placerat nisl</li><li>Consequat rhoncus</li><li>Sem nunc</li></ul></div>
  <div class="footer-col" style="left:439px"><h4>Resources</h4><ul><li>Buyer's Guide</li><li>How we guide</li><li>Contact Us</li></ul></div>
  <div class="footer-col" style="left:541px"><h4>Get Connected</h4><div class="social"><span></span><span></span><span></span><span></span></div></div>
</footer>
<div class="footer-base"><p>© 2014 Company Name &nbsp;All right reserved &nbsp;Term of Use</p></div>

</body>
</html>
```